I require a set of preaching screens for our Easter weekend.

1. Good Friday Service Title: The Lantern
2. Easter Sunday Service Title Bright Harbor
3. Message Title Screen Title Bright Harbor
Overview
We need a set of clean, minimal screen graphics for 3 service sermon series called Bright Harbor
All screens must be delivered at 1920x1080px (16:9), suitable for projection in a church auditorium.

Design style
Minimal and clean. Uncluttered. Strong typography. Subtle use of imagery or texture — nothing busy or overly decorative.

The tone should feel thoughtful and weighty without being dark or heavy.

Subtitle: Letters Along the Road to the River
Date range: 1 March – 5 April

Branding
No existing branding to match. Designer has creative freedom on colour palette and typography, provided the overall feel remains minimal and clean.
What to avoid
Busy backgrounds or heavy textures
All files in PNG at 1920x1080px
Editable source files (PSD or AI)

Please use images below as you feel is appropriate - we have permission for these - We want to see a at least three options for these screens to .

We need designs within 3 days

```html
<!DOCTYPE html>
<html lang="en">
<head>
<meta charset="utf-8">
<title>The Lantern · Bright Harbor — Screen Options</title>
<link href="https://fonts.googleapis.com/css2?family=Cinzel:wght@400;600;700&display=swap" rel="stylesheet">
<style>
  :root {
    --stage: #383838;
    --ink: #231f20;
    --gold: #f3b51c;
    --bronze: #7a4a12;
    --banner-yellow: #f2d23c;
    --paper-white: #ffffff;
    --paper-mist: #f8f8f9;
    --paper-stone: #e6e6e6;
    --band-dark: #231f20;
  }
  html, body {
    margin: 0;
    padding: 0;
    width: 1200px;
    height: 1200px;
    overflow: hidden;
    background: var(--stage);
  }
  body { position: relative; font-family: "Cinzel", "Times New Roman", serif; color: var(--ink); }

  .screen {
    position: absolute;
    left: 327px;
    width: 546px;
    height: 307px;
    overflow: hidden;
    box-shadow: 0 6px 14px rgba(0,0,0,0.35);
  }
  .screen--friday { top: 104px; background: var(--paper-white); }
  .screen--sunday { top: 451px; background: radial-gradient(ellipse 160px 110px at 55% 50%, #fff 0%, var(--paper-mist) 100%); }
  .screen--message { top: 801px; background: radial-gradient(ellipse 220px 150px at 40% 40%, #f6f6f6 0%, var(--paper-stone) 100%); }

  .title-line {
    position: absolute;
    margin: 0;
    line-height: 1;
    font-weight: 600;
    white-space: nowrap;
    letter-spacing: 0.01em;
  }
  .gilded {
    background: linear-gradient(100deg, var(--ink) 0%, var(--ink) 22%, var(--bronze) 38%, var(--gold) 52%, var(--bronze) 68%, var(--ink) 85%);
    -webkit-background-clip: text;
    background-clip: text;
    color: transparent;
  }

  /* Good Friday */
  .friday-the { left: 25px; top: 30px; font-size: 62px; }
  .friday-name { left: 27px; top: 90px; font-size: 78px; }
  .friday-subtitle {
    position: absolute; left: 26px; top: 172px; width: 330px; margin: 0;
    font-size: 20px; line-height: 27px; font-weight: 400; letter-spacing: 0.02em;
  }
  .friday-dateband {
    position: absolute; left: 0; top: 242px; width: 428px; height: 29px;
    background: linear-gradient(90deg, var(--band-dark) 0%, var(--band-dark) 20%, #8c8c8c 55%, rgba(255,255,255,0) 100%);
  }
  .friday-date {
    position: absolute; left: 26px; top: 1px; margin: 0;
    font-size: 25px; line-height: 29px; font-weight: 400; white-space: nowrap;
    background: linear-gradient(90deg, #fff 0%, #fff 45%, #e0e0e0 100%);
    -webkit-background-clip: text; background-clip: text; color: transparent;
  }
  .friday-artwork {
    position: absolute; left: 366px; top: 0; width: 155px; height: 256px;
    background: radial-gradient(ellipse 55px 80px at 55% 52%, #e2e2e2 0%, #f1f1f1 55%, rgba(255,255,255,0) 100%);
  }

  /* Sunday + Message */
  .harbor-bright { font-size: 46px; }
  .harbor-name { font-size: 62px; }
  .sunday-bright { left: 86px; top: 44px; }
  .sunday-name { left: 236px; top: 100px; }
  .sunday-glow {
    position: absolute; left: 296px; top: 24px; width: 126px; height: 72px;
    background: radial-gradient(ellipse 60px 36px at 50% 100%, rgba(243,200,40,0.45) 0%, rgba(243,200,40,0.12) 60%, rgba(248,248,249,0) 100%);
  }
  .subtitle-band {
    position: absolute; left: 0; top: 199px; width: 100%; height: 29px;
    display: flex; align-items: center; justify-content: center;
  }
  .subtitle-band--yellow { background: var(--banner-yellow); color: var(--ink); }
  .subtitle-band--dark { background: var(--band-dark); color: #fff; }
  .subtitle-band p { margin: 0; font-size: 21px; font-weight: 400; letter-spacing: 0.02em; white-space: nowrap; }
  .date-line {
    position: absolute; left: 0; width: 100%; margin: 0; text-align: center;
    font-size: 25px; line-height: 1; font-weight: 400; white-space: nowrap;
  }
  .sunday-date { top: 245px; }

  .message-bright { left: 258px; top: 44px; }
  .message-name { left: 258px; top: 100px; }
  .message-artwork {
    position: absolute; left: 60px; top: 30px; width: 146px; height: 170px;
    background: radial-gradient(ellipse 70px 85px at 50% 45%, #ffffff 0%, #f7f7f7 45%, rgba(230,230,230,0) 100%);
  }
  .message-date { top: 243px; }
</style>
</head>
<body>

  <section class="screen screen--friday" aria-label="Good Friday screen">
    <h1 class="title-line friday-the">The</h1>
    <h1 class="title-line friday-name gilded">Lantern</h1>
    <p class="friday-subtitle">Letters Along the Road to the River</p>
    <div class="friday-dateband"><p class="friday-date">1 March – 5 April</p></div>
    <div class="friday-artwork" role="img" aria-label="Soft grey figure with outstretched arms and two crosses hanging on thin cords"></div>
  </section>

  <section class="screen screen--sunday" aria-label="Easter Sunday screen">
    <div class="sunday-glow" role="img" aria-label="Golden sunrise rays"></div>
    <h1 class="title-line harbor-bright sunday-bright gilded">Bright</h1>
    <h1 class="title-line harbor-name sunday-name gilded">Harbor</h1>
    <div class="subtitle-band subtitle-band--yellow"><p>Letters Along the Road to the River</p></div>
    <p class="date-line sunday-date">1 March – 5 April</p>
  </section>

  <section class="screen screen--message" aria-label="Message title screen">
    <div class="message-artwork" role="img" aria-label="Three glowing white crosses on a hill"></div>
    <h1 class="title-line harbor-bright message-bright gilded">Bright</h1>
    <h1 class="title-line harbor-name message-name gilded">Harbor</h1>
    <div class="subtitle-band subtitle-band--dark"><p>Letters Along the Road to the River</p></div>
    <p class="date-line message-date">1 March – 5 April</p>
  </section>

</body>
</html>
```